Nest Harbor Childcare Recrutment

We need a website for candidates to sign up for jobs in childcare and alternately for nursery companies to be able to sign up to hire either temporary workers or hire permanent staff. The Temps are normally required for 1-14 days and the permanent are normally "Qualified" staff with applicable police checks and first aid, food hygiene, child welfare and safeguarding.
Updates

Target Market(s)

2 Markets. Employers: 1 - Local child day care nurseries requiring temporary staff to cover sickness, holidays, recruitment shortages. 2 - Same nurseries requiring permanent staff, normally qualified or part qualified.
Candidates: Individuals who are new to childcare or experienced seeking permanent or temporary placements.

Industry/Entity Type

Daycare

Coding

Coded - Design and coding required

Number of Pages Required

4 page

Font styles to use
Sans Serif

Colors
84c9e6

Requirements
Must have
• A split to show Employer vs Job Seeker
• Our Logo..... can send on request (See www.brambleglen.example) for idea it's similar. All part of same company.
• Board to Advertise Current Jobs
• Same day sign up, pay and get temporary staffing
• Ability for Employer or Job Seeker to fill out drop down criteria of basics
• Availability/Requirement Time
• Qualified or Unqualified
• CV email or upload
• Name
• Contact Details
Nice to have
• Testimonials
• Bits or Tasters of CVs to show employers??
Should not have
• Not sure...

```html
<!DOCTYPE html>
<html lang="en">
<head>
<meta charset="utf-8">
<title>Nest Harbor – Childcare Recruitment</title>
<link href="https://fonts.googleapis.com/css2?family=Open+Sans:wght@400;600;700&display=swap" rel="stylesheet">
<style>
:root{
  --brand:#84c9e6;
  --brand-dark:#6bb7d8;
  --ink:#222;
  --text:#444;
  --muted:#555;
  --panel:#f2f1ee;
  --white:#fff;
  --black:#111;
  --social:#3f7fa3;
}
*{box-sizing:border-box;margin:0;padding:0}
html,body{width:732px;height:1200px;overflow:hidden}
body{position:relative;background:var(--white);font-family:"Open Sans",Arial,sans-serif;color:var(--text)}
.abs{position:absolute}
/* header */
.site-header{left:0;top:0;width:732px;height:58px}
.logo{left:60px;top:18px;font-size:17px;font-weight:600;color:var(--brand)}
.main-nav{right:60px;top:27px;display:flex;gap:19px;font-size:10px;color:var(--ink)}
.main-nav .active{color:var(--brand)}
/* hero */
.hero{left:0;top:58px;width:732px;height:283px;background:linear-gradient(100deg,#4aa3d6 0%,#e9d9c7 35%,#f1e6da 55%,#c4663b 75%,#efe9e2 100%)}
.slider-arrow{top:139px;width:20px;height:20px;border-radius:50%;background:rgba(40,40,40,.85);display:flex;align-items:center;justify-content:center}
.search-panel{left:104px;top:92px;width:524px;height:106px;background:var(--brand)}
.search-panel h1{position:absolute;left:13px;top:14px;font-size:15px;font-weight:600;color:var(--white)}
.search-field{position:absolute;top:47px;height:28px;background:var(--white);font-size:7.5px;color:#333;padding-left:7px;display:flex;align-items:center}
.search-btn{position:absolute;left:424px;top:47px;width:89px;height:28px;background:var(--black);color:var(--white);font-size:7.5px;display:flex;align-items:center;justify-content:center}
/* split */
.audience{top:361px;width:280px;text-align:center}
.audience .icon{width:88px;height:88px;border-radius:50%;background:var(--brand);margin:0 auto;display:flex;align-items:center;justify-content:center}
.audience h2{margin-top:12px;font-size:16px;font-weight:600;color:var(--ink)}
.audience p{margin-top:6px;font-size:7.6px;line-height:12.5px;color:var(--muted)}
.audience .btn{display:inline-block;margin-top:11px;width:60px;height:26px;line-height:26px;background:var(--brand);color:#e8f6fc;font-size:9px;border:1px solid #a5d9ee}
.split-divider{left:368px;top:375px;width:2px;height:190px;background:linear-gradient(#fff,#e4e4e4,#fff)}
/* cards */
.card-head{background:var(--brand);color:var(--white);font-weight:600}
.jobs{left:60px;top:578px;width:269px;height:392px;background:var(--panel)}
.jobs .card-head{height:44px;font-size:12.5px;padding:14px 13px}
.job{position:absolute;left:16px;width:238px}
.job h3{font-size:12.5px;font-weight:400;color:var(--ink)}
.apply{position:absolute;right:0;top:-4px;width:52px;height:20px;background:var(--brand);color:#e8f6fc;font-size:8px;display:flex;align-items:center;justify-content:center;border:1px solid #a5d9ee}
.job dl{margin-top:8px;display:grid;grid-template-columns:94px 1fr;font-size:7.4px;line-height:12.5px;color:#333}
.more-jobs{left:15px;top:365px;font-size:9px;color:var(--brand);display:flex;align-items:center;gap:5px}
.signup{left:334px;top:579px;width:176px;height:127px;background:var(--brand);color:var(--white)}
.signup h2{position:absolute;left:14px;top:13px;font-size:12.5px;font-weight:600}
.signup p{position:absolute;left:14px;top:34px;font-size:9px}
.mail-field{position:absolute;left:13px;top:56px;width:150px;height:30px;background:var(--white);color:#333;font-size:7.4px;padding-left:7px;display:flex;align-items:center}
.dark-btn{background:var(--black);color:var(--white);font-size:7.2px;display:flex;align-items:center;justify-content:center;border-radius:2px}
.signup .dark-btn{position:absolute;left:13px;top:97px;width:36px;height:19px}
.testimonials{left:334px;top:712px;width:176px;height:258px;background:var(--panel)}
.testimonials .card-head{height:44px;font-size:12.5px;padding:13px 11px}
.testimonials p{padding:0 14px;margin-top:9px;font-size:7.4px;line-height:12.5px;color:var(--muted)}
.testimonials p+p{margin-top:12px}
.testimonials .author{position:absolute;left:17px;top:229px;font-size:8px;font-style:italic;color:#333}
.guide{left:515px;top:578px;width:157px;height:169px;background:var(--panel)}
.guide .card-head{height:44px;font-size:12.5px;padding:14px 11px}
.guide p{padding:0 13px;margin-top:9px;font-size:7.4px;line-height:12.5px;color:var(--muted)}
.guide p+p{margin-top:12px}
.guide .dark-btn{position:absolute;left:13px;top:136px;width:47px;height:19px}
.promo{left:515px;width:157px;height:90px;background:var(--brand);color:var(--white)}
.promo svg{position:absolute;left:13px}
.promo h3{position:absolute;left:47px;top:16px;font-size:12.5px;font-weight:600;line-height:14px}
.promo p{position:absolute;left:14px;font-size:7.2px;line-height:12.5px}
/* recruiters */
.recruiters-title{left:60px;top:989px;font-size:12.5px;font-weight:600;color:var(--ink)}
.round-nav{top:989px;width:19px;height:19px;border-radius:50%;border:1px solid #ddd;display:flex;align-items:center;justify-content:center}
.recruiter{top:1019px;width:115px;height:62px;border:3px solid #eee;display:flex;align-items:center;justify-content:center;font-size:11px;font-weight:700;color:#1c3f8c;text-align:center}
/* footer */
.site-footer{left:0;top:1100px;width:732px;height:100px;background:var(--brand);color:var(--white)}
.socials{position:absolute;left:293px;top:19px;display:flex;gap:9px}
.socials span{width:22px;height:22px;border-radius:50%;background:var(--social)}
.footer-nav{position:absolute;left:0;width:732px;top:54px;display:flex;justify-content:center;gap:16px;font-size:8px}
.copyright{position:absolute;left:0;width:732px;top:74px;text-align:center;font-size:7.2px}
</style>
</head>
<body>
<header class="site-header abs">
  <div class="logo abs">Nest Harbor</div>
  <nav class="main-nav abs">
    <span class="active">Home</span><span>Find a job</span><span>Jobs by email</span><span>Recruiter</span><span>Career advice</span><span>Upload your CV</span><span>Post a job</span>
  </nav>
</header>

<section class="hero abs" role="img" aria-label="Photo of a nursery carer playing with young children at a table">
  <div class="slider-arrow abs" style="left:22px"><svg width="8" height="10" viewBox="0 0 8 10"><path d="M6 1 2 5l4 4" fill="none" stroke="#fff" stroke-width="1.8"/></svg></div>
  <div class="slider-arrow abs" style="left:694px"><svg width="8" height="10" viewBox="0 0 8 10"><path d="M2 1l4 4-4 4" fill="none" stroke="#fff" stroke-width="1.8"/></svg></div>
  <form class="search-panel abs">
    <h1>Find your Job</h1>
    <div class="search-field" style="left:13px;width:151px">Enter Your Keywords</div>
    <div class="search-field" style="left:170px;width:151px">Town, City &nbsp;or Postcode</div>
    <div class="search-field" style="left:327px;width:93px;justify-content:space-between;padding-right:9px">Within 5 Miles<svg width="6" height="4" viewBox="0 0 6 4"><path d="M.5.5 3 3 5.5.5" fill="none" stroke="#333"/></svg></div>
    <div class="search-btn">Search</div>
  </form>
</section>

<section class="audience abs" style="left:58px">
  <div class="icon"><svg width="34" height="30" viewBox="0 0 34 30" fill="#fff"><circle cx="8" cy="6" r="4"/><circle cx="17" cy="5" r="5"/><circle cx="26" cy="6" r="4"/><rect x="1" y="12" width="12" height="11" rx="4"/><rect x="21" y="12" width="12" height="11" rx="4"/><rect x="9" y="12" width="16" height="17" rx="5"/></svg></div>
  <h2>Employer</h2>
  <p>Nemo enim ipsam voluptatem quia voluptas sit aspernatur aut odit aut fugit,<br>sed quia consequuntur magni dolores eos</p>
  <span class="btn">Get Jobs</span>
</section>
<div class="split-divider abs"></div>
<section class="audience abs" style="left:401px">
  <div class="icon"><svg width="24" height="30" viewBox="0 0 24 30"><rect width="24" height="30" rx="2" fill="#fff"/><g fill="#84c9e6"><rect x="5" y="4" width="2" height="2"/><rect x="9" y="4" width="2" height="2"/><rect x="13" y="4" width="2" height="2"/><rect x="17" y="4" width="2" height="2"/><rect x="5" y="9" width="2" height="2"/><rect x="9" y="9" width="2" height="2"/><rect x="13" y="9" width="2" height="2"/><rect x="17" y="9" width="2" height="2"/><rect x="5" y="14" width="2" height="2"/><rect x="9" y="14" width="2" height="2"/><rect x="13" y="14" width="2" height="2"/><rect x="17" y="14" width="2" height="2"/><rect x="9" y="22" width="6" height="8"/></g></svg></div>
  <h2>Job Seeker</h2>
  <p>Nemo enim ipsam voluptatem quia voluptas sit aspernatur aut odit aut fugit,<br>sed quia consequuntur magni dolores eos</p>
  <span class="btn">Get Hire</span>
</section>

<section class="jobs abs">
  <div class="card-head">Current Jobs</div>
  <article class="job" style="top:62px">
    <h3>Level 3 Practitioner &nbsp;(10442)</h3><span class="apply">Apply Now</span>
    <dl><dt>Setting name:</dt><dd>Little Acorn Nurseries</dd><dt>Requirement Time</dt><dd>Full Time</dd><dt>Location:</dt><dd>Mill Lane, Ashford, Kent TN1 4QX</dd><dt>Salary:</dt><dd>£6.80 - £7.05 per hour</dd><dt>Min qualification:</dt><dd>Level 3</dd></dl>
  </article>
  <article class="job" style="top:165px">
    <h3>Early Years Professional</h3><span class="apply">Apply Now</span>
    <dl><dt>Setting name:</dt><dd>Little Acorn Nurseries</dd><dt>Requirement Time</dt><dd>Full Time</dd><dt>Location:</dt><dd>Mill Lane, Ashford, Kent TN1 4QX</dd><dt>Salary:</dt><dd>£6.80 - £7.05 per hour</dd><dt>Min qualification:</dt><dd>Level 3</dd></dl>
  </article>
  <article class="job" style="top:269px">
    <h3>Room Manager</h3><span class="apply">Apply Now</span>
    <dl><dt>Setting name:</dt><dd>Little Acorn Nurseries</dd><dt>Requirement Time</dt><dd>Full Time</dd><dt>Location:</dt><dd>Mill Lane, Ashford, Kent TN1 4QX</dd><dt>Salary:</dt><dd>£6.80 - £7.05 per hour</dd><dt>Min qualification:</dt><dd>Level 3</dd></dl>
  </article>
  <div class="more-jobs abs">More Jobs <svg width="9" height="9" viewBox="0 0 9 9"><circle cx="4.5" cy="4.5" r="4.5" fill="#84c9e6"/><path d="M3.5 2.5 5.5 4.5 3.5 6.5" fill="none" stroke="#fff" stroke-width="1.3"/></svg></div>
</section>

<section class="signup abs">
  <h2>Sign up</h2>
  <p>Pay and get temporary staffing</p>
  <div class="mail-field">Enter your Mail Id</div>
  <div class="dark-btn">Submit</div>
</section>

<section class="testimonials abs">
  <div class="card-head">Testimonials</div>
  <p>Nemo enim ipsam voluptatem quia voluptas sit aspernatur aut odit aut fugit, sed quia consequuntur</p>
  <p>Neque porro quisquam est, qui dolorem ipsum quia dolor sit amet, consectetur, adipisci velit, sed quia non numquam eius modi tempora incidunt ut labore et dolore magnam aliquam quaerat voluptatem. Ut enim ad minima veniam, quis nostrum exercitationem ullam corporis suscipit laboriosam, nisi ut aliquid ex ea commodi consequatur</p>
  <div class="author">- Jane Marlow -</div>
</section>

<section class="guide abs">
  <div class="card-head">Career Guide</div>
  <p>Nemo enim ipsam voluptatem quia voluptas sit aspernatur</p>
  <p>Neque porro quisquam est, qui dolorem ipsum quia dolor sit amet, consectetur, adipisci velit</p>
  <div class="dark-btn">Read More</div>
</section>

<section class="promo abs" style="top:753px">
  <svg style="top:22px" width="26" height="20" viewBox="0 0 26 20"><rect width="26" height="20" rx="2" fill="#fff"/><path d="M1 2l12 9 12-9" fill="none" stroke="#84c9e6" stroke-width="2"/></svg>
  <h3>Get Jobs By<br>Email</h3>
  <p style="top:52px">Get the latest jobs first direct to your inbox. Sign up now.</p>
</section>

<section class="promo abs" style="top:850px">
  <svg style="top:19px" width="26" height="26" viewBox="0 0 26 26" fill="#fff"><path d="M13 0l8 8h-5v9h-6V8H5z"/><rect x="0" y="19" width="26" height="7" rx="1"/><circle cx="21" cy="22.5" r="1.3" fill="#84c9e6"/></svg>
  <h3>Upload Your<br>CV</h3>
  <p style="top:56px">Let employers and recruiters find you more easily. Upload your CV.</p>
</section>

<h2 class="recruiters-title abs">Featured Recruiters</h2>
<div class="round-nav abs" style="left:630px"><svg width="8" height="7" viewBox="0 0 8 7"><path d="M4 .5 1 3.5l3 3M7 .5 4 3.5l3 3" fill="none" stroke="#84c9e6"/></svg></div>
<div class="round-nav abs" style="left:652px"><svg width="8" height="7" viewBox="0 0 8 7"><path d="M1 .5l3 3-3 3M4 .5l3 3-3 3" fill="none" stroke="#84c9e6"/></svg></div>
<div class="recruiter abs" style="left:60px">Riverside Health</div>
<div class="recruiter abs" style="left:185px">Hollow Oak Trust</div>
<div class="recruiter abs" style="left:309px">Greenfield Grocers</div>
<div class="recruiter abs" style="left:433px">Tellwave</div>
<div class="recruiter abs" style="left:557px">Linden Stays</div>

<footer class="site-footer abs">
  <div class="socials"><span></span><span></span><span></span><span></span><span></span></div>
  <nav class="footer-nav"><span>Home</span><span>Find a job</span><span>Jobs by email</span><span>Recruiter</span><span>Career advice</span><span>Upload your CV</span><span>Post a job</span></nav>
  <p class="copyright">© 2015 Nest Harbor. All rights reserved.</p>
</footer>
</body>
</html>
```